Vesprine Oakville Cabernet Sauvignon-Wine label design

We need a package design for an up market wine brand named, Vesprine. It will be a Cabernet Sauvignon from the Oakville AVA of Napa Valley. We are looking for a stylish modern label that will stand out on a retail shelf. We want the label to be attention grabbing and stylish while presenting an up market luxury brand.

Sick

Requirements
Must have
• Must have the words(in order of importance)
-Vesprine
-Cabernet Sauvignon
-Oakville
-Napa Valley
-2018

Must be designed for a traditional "Bordeaux" style bottle (Bottle specs in uploaded files)
Should not have
• Any images of grapes, vineyards, wine glasses or bottles

```html
<!DOCTYPE html>
<html lang="en">
<head>
<meta charset="utf-8">
<title>Vesprine Oakville Cabernet Sauvignon – Label</title>
<link href="https://fonts.googleapis.com/css2?family=Saira+Condensed:wght@500;600;700&display=swap" rel="stylesheet">
<style>
  :root {
    --backdrop: #e4e1dc;
    --label-black: #050505;
    --varietal-red: #c8203a;
    --text-white: #ffffff;
    --vintage-red: #d0283a;
    --tone-wine: #7e1621;
    --tone-coral: #e35a6a;
    --tone-teal: #3f857b;
    --tone-gold: #c99a34;
    --tone-umber: #6a3022;
  }
  * { margin: 0; padding: 0; box-sizing: border-box; }
  html, body {
    width: 1200px;
    height: 1000px;
    overflow: hidden;
    background: var(--backdrop);
  }
  .canvas {
    position: relative;
    width: 1200px;
    height: 1000px;
  }
  .wine-label {
    position: absolute;
    left: 352px;
    top: 60px;
    width: 496px;
    height: 880px;
    font-family: "Saira Condensed", "Arial Narrow", sans-serif;
  }
  .varietal-tab {
    position: absolute;
    left: 0;
    top: 0;
    width: 322px;
    height: 70px;
    background: var(--varietal-red);
    color: var(--text-white);
    display: flex;
    align-items: center;
    justify-content: center;
    font-weight: 600;
    font-size: 24px;
    letter-spacing: 4px;
    z-index: 2;
  }
  .label-body {
    position: absolute;
    left: 0;
    top: 58px;
    width: 496px;
    height: 822px;
    background: var(--label-black);
  }
  .colour-field {
    position: absolute;
    left: 0;
    top: 46px;
    width: 478px;
    height: 374px;
    background: linear-gradient(180deg,
      var(--tone-wine) 0%,
      var(--tone-coral) 28%,
      var(--tone-teal) 52%,
      var(--tone-gold) 74%,
      var(--tone-umber) 100%);
  }
  .brand-name {
    position: absolute;
    left: 0;
    right: 0;
    top: 470px;
    text-align: center;
    color: var(--text-white);
    font-weight: 600;
    font-size: 88px;
    letter-spacing: 3px;
    line-height: 1;
    text-transform: uppercase;
  }
  .vintage {
    position: absolute;
    left: 0;
    right: 0;
    top: 712px;
    text-align: center;
    color: var(--vintage-red);
    font-weight: 500;
    font-size: 20px;
    letter-spacing: 2px;
  }
  .appellation {
    position: absolute;
    left: 0;
    right: 0;
    top: 742px;
    color: var(--text-white);
    font-weight: 600;
    font-size: 24px;
    letter-spacing: 3px;
    display: flex;
    justify-content: center;
    align-items: center;
    gap: 12px;
  }
  .appellation .dot {
    width: 10px;
    height: 10px;
    border-radius: 50%;
    background: var(--text-white);
  }
</style>
</head>
<body>
  <div class="canvas">
    <div class="wine-label">
      <div class="varietal-tab">CABERNET SAUVIGNON</div>
      <div class="label-body">
        <div class="colour-field" role="img" aria-label="Decorative band of horizontal colour stripes in wine red, coral, pink, teal, gold and brown"></div>
        <div class="brand-name">Vesprine</div>
        <div class="vintage">2018</div>
        <div class="appellation">
          <span>OAKVILLE</span><span class="dot"></span><span>NAPA VALLEY</span>
        </div>
      </div>
    </div>
  </div>
</body>
</html>
```